Larkspur Ridge Management - Business Cards

I need business cards. My current logo was designed by a designer at this site and I very much like and am happy with the results. I would like a business card that is trendy, unique, current yet professional. I deal with high net worth clients daily

Target Market(s)

Out of state investors looking to get into the rental market in Ohio

Industry/Entity Type

Property Management, Consulting

Contact Information for Business Card

Name, Title (Chief Financial Officer) office phone number (555) 817-3094 website address larkridgemgmt.example

Font styles to use
Sans Serif

Colors
0054AA
0677BA
7BADD7
CADEEF
E8F1F8
0094D4
00A9DD
6FCCEA
C7EBF8
E9F6FB
00AB8E
00BBA5
67D7C9
C6EFE9
E9F9F6

```html
<!DOCTYPE html>
<html lang="en">
<head>
<meta charset="utf-8">
<title>Larkspur Ridge Management – Business Card</title>
<link rel="stylesheet" href="https://fonts.googleapis.com/css2?family=Cabin:wght@400;700&display=swap">
<style>
  :root {
    --navy: #12246b;
    --ink: #0d2150;
    --icon: #0b2350;
    --text-grey: #3a3d45;
    --bg-shade: #c9c9c9;
    --bg-light: #ffffff;
    --wave-deep: #0a5a86;
    --wave-mid: #0677BA;
    --wave-bright: #00A9DD;
    --wave-cyan: #12c6dc;
    --wave-pale: #6FCCEA;
    --wave-blue: #0054AA;
    --halo: #8f95c6;
    --white: #ffffff;
  }
  html, body { margin: 0; padding: 0; overflow: hidden; background: #ffffff; }
  .card {
    position: relative;
    width: 1200px;
    height: 686px;
    overflow: hidden;
    font-family: "Cabin", sans-serif;
    background:
      radial-gradient(ellipse 900px 420px at 420px 560px, var(--bg-light) 45%, rgba(255,255,255,0) 100%),
      linear-gradient(160deg, var(--bg-shade) 0%, #e6e6e6 35%, #f4f4f4 60%, var(--bg-light) 100%);
  }
  .card__art { position: absolute; inset: 0; width: 1200px; height: 686px; }
  .identity { position: absolute; left: 81px; top: 100px; color: var(--ink); }
  .identity__name { margin: 0; font-size: 52px; font-weight: 700; line-height: 1; letter-spacing: 0.5px; }
  .identity__title { margin: 16px 0 0; font-size: 30px; font-weight: 400; letter-spacing: 0.6px; }
  .contacts { position: absolute; left: 82px; top: 276px; margin: 0; padding: 0; list-style: none; }
  .contact { display: flex; align-items: flex-start; height: 71px; margin-bottom: 43px; }
  .contact__icon {
    width: 71px; height: 71px; border-radius: 13px; background: var(--icon);
    display: flex; align-items: center; justify-content: center; flex-shrink: 0;
  }
  .contact__text { margin-left: 37px; margin-top: -4px; font-size: 30px; color: var(--text-grey); letter-spacing: 0.4px; }
  .brand {
    position: absolute; left: 938px; top: 170px; width: 180px;
    text-align: center; color: var(--white);
    font-size: 22px; font-weight: 700; line-height: 1.25; letter-spacing: 0.5px;
  }
</style>
</head>
<body>
  <div class="card">
    <svg class="card__art" viewBox="0 0 1200 686" aria-hidden="true">
      <path d="M1200 230 C1010 260 760 380 765 686 L1200 686 Z" fill="var(--wave-deep)"/>
      <path d="M1200 300 C1060 330 850 430 855 686 L1200 686 Z" fill="var(--wave-mid)" opacity="0.9"/>
      <path d="M1200 330 C1080 360 890 460 900 686 L1200 686 Z" fill="var(--wave-cyan)"/>
      <path d="M1200 360 C1100 390 950 480 965 686 L1200 686 Z" fill="var(--wave-bright)" opacity="0.85"/>
      <path d="M1200 420 C1120 440 1010 520 1030 686 L1200 686 Z" fill="var(--wave-mid)"/>
      <path d="M1200 470 C1150 500 1090 560 1110 686 L1200 686 Z" fill="var(--wave-blue)"/>
      <path d="M880 420 C900 520 940 600 990 686" stroke="var(--wave-pale)" stroke-width="5" fill="none" opacity="0.7"/>
      <path d="M960 450 C990 540 1030 610 1080 686" stroke="var(--wave-pale)" stroke-width="4" fill="none" opacity="0.6"/>
      <circle cx="1030" cy="240" r="270" fill="var(--halo)" opacity="0.85"/>
      <circle cx="1050" cy="245" r="265" fill="var(--navy)"/>
    </svg>

    <div class="identity">
      <h1 class="identity__name">Your Name</h1>
      <p class="identity__title">Chief Financial Officer</p>
    </div>

    <ul class="contacts">
      <li class="contact">
        <span class="contact__icon">
          <svg width="40" height="48" viewBox="0 0 40 48" aria-hidden="true">
            <path d="M9 3 L15 3 L17 15 L12 18 C14 26 18 32 24 37 L29 33 L37 40 L33 46 C20 46 4 28 4 10 Z" fill="var(--white)"/>
          </svg>
        </span>
        <span class="contact__text">(555) 817-3094</span>
      </li>
      <li class="contact">
        <span class="contact__icon">
          <svg width="46" height="32" viewBox="0 0 46 32" aria-hidden="true">
            <rect x="1" y="1" width="44" height="30" fill="var(--white)"/>
            <path d="M1 2 L23 18 L45 2" stroke="var(--icon)" stroke-width="3" fill="none"/>
          </svg>
        </span>
        <span class="contact__text">larkridgemgmt.example</span>
      </li>
      <li class="contact">
        <span class="contact__icon"></span>
      </li>
    </ul>

    <div class="brand">Larkspur Ridge Management</div>
  </div>
</body>
</html>
```